Corporate PowerPoint Template

Seeking a Powerpoint Template Design for High Technology company based in Silicon Valley. We are seeking a general template design that conveys a professional, clean, progressive message.

The Template must have the following elements at a minimum:
1. Title Page (see comments following)
2. Agenda Page
3. Page Number, Date and Confidentiality Statement
Items in #3 are to appear on all pages except title page

We expect the Title page to be graphical in nature with area for Presentation Title, Presenter Name, Date and a place for confidentiality statement should be present as well. Three (3) distinct Title pages to address different constituencies: Customers, Partners and Internal Communications.

In general, we would like to stay with our corporate color scheme (which may be found in our logo). To better understand our products, logo and look and feel - please visit our website at: http://www.velmarotek.example

```html
<!DOCTYPE html>
<html lang="en">
<head>
<meta charset="utf-8">
<title>Velmarotek Presentation Template</title>
<link href="https://fonts.googleapis.com/css2?family=Roboto:ital,wght@0,300;0,400;0,700;1,400;1,700&display=swap" rel="stylesheet">
<style>
:root{
  --board:#a9abae;
  --paper:#ffffff;
  --header:#2d6893;
  --blue:#1673c0;
  --navy:#2d5f8a;
  --teal:#17899a;
  --teal-light:#3f95a8;
  --slate:#6d6d6d;
  --bar:#d9d9d9;
  --ink:#555;
  --muted:#999;
  --rule:#cfcfcf;
}
*{margin:0;padding:0;box-sizing:border-box}
html,body{width:1200px;height:900px;overflow:hidden}
body{background:var(--board);font-family:"Roboto",Arial,sans-serif;color:var(--ink);position:relative}
.slide{position:absolute;width:374px;height:288px;background:var(--paper);overflow:hidden}
.s-welcome{left:26px;top:142px}
.s-agenda{left:412px;top:142px}
.s-alt{left:797px;top:142px}
.s-about{left:26px;top:442px}
.s-team{left:412px;top:438px}
.s-thanks{left:797px;top:442px}
.slide-header{position:absolute;left:0;top:0;width:100%;height:26px;background:var(--header);color:#fff;font-weight:300;font-size:14px;padding:8px 0 0 16px;line-height:14px;text-transform:uppercase}
.bottom-band{position:absolute;left:0;bottom:0;width:100%;height:4px;background:var(--header)}
.deco{position:absolute;left:0;top:0}
.abs{position:absolute}
.brand{display:flex;align-items:center;gap:5px;color:var(--navy);font-weight:300}
.brand .mark{border-radius:50%;background:var(--teal);flex:none}
/* footer */
.slide-footer{position:absolute;left:14px;right:14px;top:271px;border-top:1px solid var(--rule);padding-top:3px;display:flex;justify-content:space-between;align-items:center;font-size:4.5px;color:var(--muted)}
.slide-footer .left{display:flex;align-items:center;gap:5px}
.slide-footer .brand{font-size:6px;gap:2px}
.slide-footer .brand .mark{width:6px;height:6px}
/* welcome */
.welcome-title{left:21px;top:124px;font-size:16px;font-weight:300;color:var(--navy);letter-spacing:-.3px}
.welcome-sub{left:21px;top:142px;font-size:10px;font-weight:300;color:var(--navy);letter-spacing:1px}
.welcome-date{left:21px;top:159px;font-size:8px;font-weight:300;color:var(--muted)}
.welcome-legal{left:21px;top:264px;font-size:4.8px;line-height:7px;color:var(--ink)}
.hero-brand{left:210px;top:147px;width:104px;justify-content:center;font-size:15px}
.hero-brand .mark{width:18px;height:18px}
/* agenda */
.agenda-list{list-style:none;position:absolute;left:70px;top:90px}
.agenda-item{position:relative;height:21px;margin-bottom:8.5px;display:flex;align-items:center}
.agenda-item .num{width:20px;height:20px;border-radius:50%;background:var(--teal);border:1.5px solid #cfe6ea;color:#fff;font-size:11px;font-weight:300;display:flex;align-items:center;justify-content:center;position:relative;z-index:1}
.agenda-item .label{margin-left:-2px;width:214px;height:21px;background:var(--bar);font-size:10px;font-weight:300;color:#666;padding-left:18px;line-height:21px;text-transform:uppercase}
/* alt agenda */
.alt-list{list-style:none;position:absolute;left:78px;top:76px}
.alt-item{display:flex;align-items:center;height:35px}
.alt-item .icon{width:28px;height:28px;border-radius:50%;display:flex;align-items:center;justify-content:center}
.alt-item .link{width:14px;height:1px;background:#bbb;position:relative}
.alt-item .link::after{content:"";position:absolute;right:-2px;top:-1.5px;width:4px;height:4px;border-radius:50%;background:var(--navy)}
.alt-item .text{border-left:1px solid #ccc;padding-left:8px;margin-left:0;height:28px;display:flex;flex-direction:column;justify-content:center}
.alt-item h3{font-size:6.8px;font-weight:400;color:var(--blue);text-transform:uppercase}
.alt-item p{font-size:4.3px;line-height:6px;color:var(--muted);width:122px}
.i-teal{background:var(--teal)}.i-navy{background:var(--navy)}.i-light{background:var(--teal-light)}.i-blue{background:var(--blue)}.i-slate{background:var(--slate)}
/* about */
.about-photo{left:20px;top:61px;width:348px;height:79px;background:linear-gradient(90deg,#9a9a9a,#d8d8d8 35%,#8c8c8c 60%,#e4e4e4)}
.about-lead{left:19px;top:154px;width:120px;font-size:6px;line-height:10px;color:var(--blue);text-transform:uppercase}
.about-body{left:146px;top:154px;width:214px;font-size:5.5px;line-height:10px;color:var(--ink);text-align:justify;font-weight:300}
.about-body p+p{margin-top:10px}
/* team */
.team-intro{left:20px;top:70px;width:334px;text-align:center;font-size:5.5px;line-height:10.5px;font-weight:700;font-style:italic;color:#333}
.member{position:absolute;top:106px;width:90px;text-align:center}
.member .portrait{width:56px;height:56px;margin:0 auto;border-radius:50%;border:2px solid var(--navy);padding:2px;background:#fff}
.member .portrait div{width:100%;height:100%;border-radius:50%;background:radial-gradient(circle at 50% 40%,#e9e9e9,#8e8e8e)}
.member h3{margin-top:6px;font-size:7.5px;font-weight:400;color:#1a7aa5;text-transform:uppercase}
.member .role{font-size:4.8px;font-style:italic;color:#333}
.member p.bio{margin:9px auto 0;width:76px;font-size:4.8px;line-height:10.4px;color:#aaa;text-align:justify;font-weight:300}
/* thanks */
.thanks-brand{left:21px;top:130px;font-size:16px}
.thanks-brand .mark{width:20px;height:20px}
.contacts{position:absolute;left:21px;top:167px;list-style:none}
.contacts li{display:flex;align-items:center;gap:4px;font-size:8.5px;font-weight:300;color:#333;height:14.5px}
.contacts svg{flex:none}
.social{position:absolute;left:21px;top:219px;display:flex;gap:4px}
.social span{width:12px;height:12px;border-radius:2px;background:var(--navy)}
.thanks-label{left:208px;top:148px;width:108px;text-align:center;font-size:13px;font-weight:300;color:#fff;text-transform:uppercase}
</style>
</head>
<body>

<!-- Title slide -->
<section class="slide s-welcome">
  <svg class="deco" width="374" height="288" viewBox="0 0 374 288">
    <path d="M103 0 Q170 105 262 157 Q320 188 374 198" fill="none" stroke="#b9b9b9" stroke-width=".6"/>
    <polyline points="156,156 169,176 186,198" fill="none" stroke="#b9b9b9" stroke-width=".6"/>
    <line x1="186" y1="198" x2="166" y2="214" stroke="#b9b9b9" stroke-width=".6"/>
    <line x1="204" y1="183" x2="186" y2="198" stroke="#b9b9b9" stroke-width=".6"/>
    <line x1="318" y1="140" x2="350" y2="116" stroke="#b9b9b9" stroke-width=".6"/>
    <line x1="21" y1="155" x2="156" y2="155" stroke="#888" stroke-width=".6"/>
    <circle cx="262" cy="157" r="57" fill="#fff" stroke="var(--blue)" stroke-width="5"/>
    <circle cx="350" cy="116" r="10" fill="var(--teal)"/>
    <circle cx="156" cy="156" r="2.4" fill="#777"/>
    <circle cx="169" cy="176" r="4" fill="var(--blue)"/>
    <circle cx="186" cy="198" r="9.5" fill="var(--navy)"/>
    <circle cx="166" cy="214" r="4" fill="var(--teal)"/>
  </svg>
  <div class="abs brand hero-brand"><span class="mark"></span>velmarotek</div>
  <h1 class="abs welcome-title">WELCOME</h1>
  <p class="abs welcome-sub">To Our Presentation</p>
  <p class="abs welcome-date">August 2014</p>
  <p class="abs welcome-legal">Copyright © 2014 velmarotek, All rights reserved. Contains confidential and proprietary information<br>and may not be disclosed or reproduced without the prior written consent of velmarotek</p>
  <div class="bottom-band"></div>
</section>

<!-- Agenda -->
<section class="slide s-agenda">
  <h2 class="slide-header">Agenda</h2>
  <ol class="agenda-list">
    <li class="agenda-item"><span class="num">1</span><span class="label">Lorem ipsum dolor sit met</span></li>
    <li class="agenda-item"><span class="num">2</span><span class="label">Lorem ipsum dolor sit met</span></li>
    <li class="agenda-item"><span class="num">3</span><span class="label">Lorem ipsum dolor sit met</span></li>
    <li class="agenda-item"><span class="num">4</span><span class="label">Lorem ipsum dolor sit met</span></li>
    <li class="agenda-item"><span class="num">5</span><span class="label">Lorem ipsum dolor sit met</span></li>
  </ol>
  <footer class="slide-footer"><div class="left"><span class="brand"><span class="mark"></span>velmarotek</span><span>Copyright © 2014 velmarotek, All rights reserved</span></div><span>8/30/2014 | 2</span></footer>
</section>

<!-- Alternative agenda -->
<section class="slide s-alt">
  <h2 class="slide-header">Alternative Agenda</h2>
  <ul class="alt-list">
    <li class="alt-item"><span class="icon i-teal"><svg width="14" height="14" viewBox="0 0 14 14" fill="none" stroke="#fff" stroke-width="1.3"><circle cx="7" cy="7" r="5.5"/><circle cx="7" cy="7" r="3"/><circle cx="7" cy="7" r=".8" fill="#fff"/><line x1="7" y1="7" x2="12.5" y2="1.5"/></svg></span><span class="link"></span><div class="text"><h3>Lorem ipsum dolor sit met</h3><p>Lorem ipsum dolor sit amet, conse ctetur adipiscing elit, sed do eiusmod tempor incididunt ut labore</p></div></li>
    <li class="alt-item"><span class="icon i-navy"><svg width="14" height="14" viewBox="0 0 14 14"><path d="M4.5 6V4.5a2.5 2.5 0 0 1 5 0V6" fill="none" stroke="#fff" stroke-width="1.3"/><rect x="3" y="6" width="8" height="6" rx="1" fill="#fff"/></svg></span><span class="link"></span><div class="text"><h3>Lorem ipsum dolor sit met</h3><p>Lorem ipsum dolor sit amet, conse ctetur adipiscing elit, sed do eiusmod tempor incididunt ut labore</p></div></li>
    <li class="alt-item"><span class="icon i-light"><svg width="14" height="14" viewBox="0 0 14 14" fill="none" stroke="#fff" stroke-width="1.6"><circle cx="8.5" cy="5.5" r="3.5"/><line x1="6" y1="8" x2="2" y2="12"/></svg></span><span class="link"></span><div class="text"><h3>Lorem ipsum dolor sit met</h3><p>Lorem ipsum dolor sit amet, conse ctetur adipiscing elit, sed do eiusmod tempor incididunt ut labore</p></div></li>
    <li class="alt-item"><span class="icon i-blue"><svg width="14" height="14" viewBox="0 0 14 14" fill="none" stroke="#fff" stroke-width="1.3"><path d="M2 8l2-5h6l2 5v4H2z"/><path d="M2 8h3l1 1.5h2L9 8h3"/><path d="M7 2v4M5.5 4.5L7 6l1.5-1.5"/></svg></span><span class="link"></span><div class="text"><h3>Lorem ipsum dolor sit met</h3><p>Lorem ipsum dolor sit amet, conse ctetur adipiscing elit, sed do eiusmod tempor incididunt ut labore</p></div></li>
    <li class="alt-item"><span class="icon i-slate"><svg width="14" height="14" viewBox="0 0 14 14" fill="#fff"><circle cx="7" cy="5" r="2.8"/><path d="M2 13c0-3 2.2-5 5-5s5 2 5 5z"/></svg></span><span class="link"></span><div class="text"><h3>Lorem ipsum dolor sit met</h3><p>Lorem ipsum dolor sit amet, conse ctetur adipiscing elit, sed do eiusmod tempor incididunt ut labore</p></div></li>
  </ul>
  <footer class="slide-footer"><div class="left"><span class="brand"><span class="mark"></span>velmarotek</span><span>Copyright © 2014 velmarotek, All rights reserved</span></div><span>8/30/2014 | 2</span></footer>
</section>

<!-- About us -->
<section class="slide s-about">
  <h2 class="slide-header">About Us</h2>
  <div class="abs about-photo" role="img" aria-label="Black and white photo of a business team working together at a table"></div>
  <p class="abs about-lead">Lorem ipsum dolor sit met consectur adipiscing elit, sed do euismod tempor incididunt ut labore et dolore magna</p>
  <div class="abs about-body">
    <p>Lorem ipsum dolor sit amet, consectetur adipisicing elit, sed do eiusmod tempor incididunt ut labore et dolore magna aliqua. Ut enim ad minim veniam, quis nostrud exercitation ullamco laboris nisi ut aliquip ex ea commodo consequat. Duis aute irure dolor in reprehenderit in voluptate velit esse cillum dolore eu fugiat nulla pariatur.</p>
    <p>Lorem ipsum dolor sit amet, consectetur adipisicing elit, sed do eiusmod tempor incididunt ut labore et dolore magna aliqua. Ut enim ad minim veniam, quis nostrud exercitation ullamco laboris nisi ut aliquip ex ea commodo consequat. Duis aute irure dolor in reprehenderit in voluptate velit esse cillum dolore eu.</p>
  </div>
  <footer class="slide-footer"><div class="left"><span class="brand"><span class="mark"></span>velmarotek</span><span>Copyright © 2014 velmarotek, All rights reserved</span></div><span>8/30/2014 | 2</span></footer>
</section>

<!-- Our team -->
<section class="slide s-team">
  <h2 class="slide-header">Our Team</h2>
  <p class="abs team-intro">dolor sit amet, consectetur adipisicing elit, sed do eiusmod tempor incididunt ut labore et dolore magna aliqua.<br>Ut enim ad minim veniam, quis nostrud exercitation ullamco laboris nisi ut a</p>
  <article class="member" style="left:27px">
    <div class="portrait"><div role="img" aria-label="Portrait photo of Jonathan Doe"></div></div>
    <h3>Jonathan Doe</h3><p class="role">President</p>
    <p class="bio">dolor sit amet, consectetur adipiscing elit, sed do eiusmod tempor incididunt ut labore et dolore magna aliqua. Ut enim ad minim veniam, quis nostrud exercitation</p>
  </article>
  <article class="member" style="left:142px">
    <div class="portrait"><div role="img" aria-label="Portrait photo of Melanie Doe"></div></div>
    <h3>Melanie Doe</h3><p class="role">CEO / Founder</p>
    <p class="bio">dolor sit amet, consectetur adipiscing elit, sed do eiusmod tempor incididunt ut labore et dolore magna aliqua. Ut enim ad minim veniam, quis nostrud exercitation</p>
  </article>
  <article class="member" style="left:253px">
    <div class="portrait"><div role="img" aria-label="Portrait photo of Natalie Doe"></div></div>
    <h3>Natalie Doe</h3><p class="role">Vice President</p>
    <p class="bio">dolor sit amet, consectetur adipiscing elit, sed do eiusmod tempor incididunt ut labore et dolore magna aliqua. Ut enim ad minim veniam, quis nostrud exercitation</p>
  </article>
  <footer class="slide-footer"><div class="left"><span class="brand"><span class="mark"></span>velmarotek</span><span>Copyright © 2014 velmarotek, All rights reserved</span></div><span>8/30/2014 | 2</span></footer>
</section>

<!-- Thank you -->
<section class="slide s-thanks">
  <svg class="deco" width="374" height="288" viewBox="0 0 374 288">
    <path d="M103 0 Q170 105 262 157 Q320 188 374 198" fill="none" stroke="#b9b9b9" stroke-width=".6"/>
    <polyline points="155,157 169,175 186,198" fill="none" stroke="#b9b9b9" stroke-width=".6"/>
    <line x1="186" y1="198" x2="166" y2="214" stroke="#b9b9b9" stroke-width=".6"/>
    <line x1="206" y1="182" x2="186" y2="198" stroke="#b9b9b9" stroke-width=".6"/>
    <line x1="320" y1="138" x2="350" y2="117" stroke="#b9b9b9" stroke-width=".6"/>
    <circle cx="262" cy="157" r="60" fill="#d6d6d6"/>
    <circle cx="262" cy="157" r="54" fill="var(--blue)"/>
    <circle cx="350" cy="117" r="10" fill="var(--teal)"/>
    <circle cx="155" cy="157" r="2.4" fill="#777"/>
    <circle cx="169" cy="175" r="4" fill="var(--blue)"/>
    <circle cx="186" cy="198" r="9.5" fill="var(--navy)"/>
    <circle cx="166" cy="214" r="4" fill="var(--teal)"/>
  </svg>
  <div class="abs brand thanks-brand"><span class="mark"></span>velmarotek</div>
  <ul class="contacts">
    <li><svg width="9" height="9" viewBox="0 0 10 10" fill="none" stroke="var(--navy)" stroke-width="1"><circle cx="5" cy="5" r="4.4"/><rect x="2.6" y="3.4" width="4.8" height="3.4"/><path d="M2.6 3.4L5 5.3l2.4-1.9"/></svg>info@velmarotek.example</li>
    <li><svg width="9" height="9" viewBox="0 0 10 10" fill="none" stroke="var(--navy)" stroke-width="1"><circle cx="5" cy="5" r="4.4"/><ellipse cx="5" cy="5" rx="2" ry="4.4"/><line x1=".6" y1="5" x2="9.4" y2="5"/></svg>www.velmarotek.example</li>
    <li><svg width="9" height="9" viewBox="0 0 10 10"><circle cx="5" cy="5" r="4.8" fill="var(--navy)"/><path d="M2.8 4.2h4.4v2.6H2.8z" fill="#fff"/><circle cx="5" cy="5.5" r=".8" fill="var(--navy)"/></svg>555-014-2290</li>
  </ul>
  <div class="social" aria-label="Social media links"><span></span><span></span><span></span></div>
  <p class="abs thanks-label">Thank You</p>
  <div class="bottom-band"></div>
</section>

</body>
</html>
```